Creation of a construction/bricklaying business website

Following the template format of "Wendmoor 2", the following content would need to be included:
1. Landing page with 3 tiles that go to their own pages.
- Landing page to include background photo and description of services offered.
2. 3 tiles to include:
a) "Contact Us For A Free Quote or Friendly Discussion" Form (middle tile)
b) Case Studies and Testimonials
c) Certifications and Professional Membership
- Design logo to be used from previous PixelHarbor project. Example of logo attached below, please access full JPG files from our account.

Target Market(s)

Prospective clients seeking construction work (bricklaying speciality)

Industry/Entity Type

Residential Construction

Coding

Coded - Design and coding required

Number of Pages Required

4 page

Font styles to use
Sans Serif

Colors

Designer to choose colors to be used in the design.

Requirements
Must have
• Following the template format of "Wendmoor 2", the following content would need to be included:
• 1. Landing parent page with 3 tiles that go to the 3 child pages.
• - Landing page to include background photo and description of services offered.
• 2. 3 tiles to include:
• a) "Contact Us For A Free Quote or Friendly Discussion" Form (middle tile)
• b) Case Studies and Testimonials (first tile / left side)
• c) Certifications and Professional Memberships (third tile / right side) (This should include logos of the relevant organisations being displayed. Specifically QLT and the Keystone Pact QLT).
• - Design logo to be used from previous PixelHarbor project. Example of logo attached below, please access full JPG files from our account.
Nice to have
• Sleek and modern feel.
• Approachable in terms of how people can contact the company for a quote.
• Traditional pictures to give credibility and comfort around choosing this company.
Should not have
• Cheesy pictures
• Over-complicated
• Simple to use
• Easy URL domain name

```html
<!DOCTYPE html>
<html lang="en">
<head>
<meta charset="utf-8">
<title>R.T Harlow Construction LTD</title>
<link rel="stylesheet" href="https://fonts.googleapis.com/css2?family=Montserrat:wght@500;600;700&family=Questrial&display=swap">
<style>
:root{
  --blue:#0f5ca8;
  --nav:#0c58a4;
  --ink:#1b1b1b;
  --muted:#8a8a8a;
  --page:#efefef;
  --white:#ffffff;
  --panel:#f1f1f1;
  --sky:#cfe8f4;
  --tag:#1170aa;
  --foot:#2b2b2b;
  --foot-deep:#1d1d1d;
  --foot-text:#9a9a9a;
}
*{box-sizing:border-box;margin:0;padding:0}
html,body{width:1200px;height:2624px;overflow:hidden}
body{background:var(--page);font-family:"Questrial",Arial,sans-serif;color:var(--ink);position:relative}
.abs{position:absolute}
.heading{font-family:"Montserrat",Arial,sans-serif;font-weight:700;text-transform:uppercase;color:var(--ink)}

/* top bar */
.welcome{left:0;top:0;width:1200px;height:23px;background:#e9e9e9;font-size:11px;text-align:center;line-height:23px;color:#333}
.header{left:0;top:23px;width:1200px;height:103px;background:var(--white)}
.brand{left:505px;top:26px;display:flex;align-items:center;gap:10px;color:var(--blue);font-family:"Montserrat",Arial,sans-serif;font-weight:700}
.brand-mark{width:18px;height:18px;background:var(--blue)}
.brand-name{font-size:30px;line-height:30px;letter-spacing:-0.5px}
.brand-sub{font-size:11px;line-height:14px;letter-spacing:1.4px;text-align:right}
.search{left:833px;top:35px;width:206px;height:31px;border:1px solid #e2e2e2;background:#fafafa;font-size:10px;color:#bbb;padding:0 10px;line-height:29px}
.search svg{position:absolute;right:9px;top:9px}
.nav{left:0;top:126px;width:1200px;height:35px;background:var(--nav)}
.nav a{position:absolute;top:0;line-height:35px;color:#fff;font-family:"Montserrat",Arial,sans-serif;font-weight:600;font-size:11px;text-decoration:none;transform:translateX(-50%);white-space:nowrap}

/* hero */
.hero-side{top:161px;height:434px;width:161px}
.hero-left{left:0;background:linear-gradient(160deg,#3c4350,#1b2029 60%,#4a3a2b)}
.hero-right{left:1039px;background:linear-gradient(200deg,#2e3a48,#1a222d 55%,#5a4630)}
.hero-main{left:161px;top:161px;width:878px;height:434px;background:linear-gradient(110deg,#1b4a9c 0%,#2f66c4 35%,#5a8ee0 55%,#1d3f8a 80%,#101f55 100%)}
.arrow{top:356px;width:40px;height:40px;border-radius:50%;background:#fff;display:flex;align-items:center;justify-content:center}

/* content */
.sheet{left:161px;top:595px;width:878px;height:1226px;background:var(--white)}
.title-row{left:217px;width:766px;display:flex;align-items:center;gap:16px}
.title-row::before,.title-row::after{content:"";flex:1;height:3px;background:var(--blue)}
.title-row span{font-family:"Montserrat",Arial,sans-serif;font-weight:700;font-size:19px;text-transform:uppercase;white-space:nowrap}
.service{top:700px;width:100px;text-align:center;transform:translateX(-50%)}
.service svg{display:block;margin:0 auto;height:62px}
.service p{margin-top:42px;font-family:"Montserrat",Arial,sans-serif;font-weight:700;font-size:11px;text-transform:uppercase}
.service i{display:block;margin:10px auto 0;width:90px;height:3px;background:var(--blue)}

.case{top:904px;width:439px;height:298px;text-align:center;color:#fff}
.case .kicker{margin-top:103px;font-family:"Montserrat",Arial,sans-serif;font-size:11px;letter-spacing:2.5px;text-transform:uppercase;font-weight:600}
.case h3{margin-top:6px;font-family:"Montserrat",Arial,sans-serif;font-size:19px;font-weight:700;text-transform:uppercase}
.case .more{display:inline-block;margin-top:24px;padding:10px 8px;border-top:2px solid #fff;border-bottom:2px solid #fff;font-family:"Montserrat",Arial,sans-serif;font-size:10px;font-weight:700}
.case-one{left:161px;background:linear-gradient(180deg,#5f6b7c 0%,#3d3429 55%,#2f6f8a 100%)}
.case-two{left:600px;background:linear-gradient(180deg,#55657a 0%,#6b737d 50%,#3f7f95 100%)}

.card{top:1305px;width:243px;height:232px;background:var(--panel)}
.card .photo{height:143px}
.card h4{margin:14px 0 0 15px;font-family:"Montserrat",Arial,sans-serif;font-weight:600;font-size:14px}
.card .more{display:inline-block;margin:12px 0 0 15px;font-family:"Montserrat",Arial,sans-serif;font-weight:700;font-size:9px;text-transform:uppercase;padding-bottom:4px;border-bottom:3px solid var(--ink)}

.field{top:1660px;height:36px;border:1px solid #e4e4e4;box-shadow:0 1px 3px rgba(0,0,0,.08);background:#fff;font-size:10px;color:#999;line-height:34px;padding-left:14px}
.submit{left:568px;top:1717px;width:58px;height:33px;border-top:2px solid var(--ink);border-bottom:2px solid var(--ink);font-family:"Montserrat",Arial,sans-serif;font-weight:700;font-size:9px;text-align:center;line-height:29px}

/* certification */
.cert{left:161px;top:1821px;width:878px;height:430px;background:var(--sky)}
.cert-text{left:191px;top:1911px;width:818px;text-align:center;font-family:"Montserrat",Arial,sans-serif;font-weight:600;font-size:12px;line-height:19px}
.cert-sub{left:161px;top:1964px;width:878px;text-align:center;font-family:"Montserrat",Arial,sans-serif;font-weight:600;font-size:14px;color:var(--blue)}
.tag{height:29px;line-height:29px;background:#fff;font-family:"Montserrat",Arial,sans-serif;font-weight:600;font-size:11px;text-align:center;box-shadow:0 1px 2px rgba(0,0,0,.08)}
.tag.on{background:var(--tag);color:#fff}
.badge{top:2085px;height:91px;background:#fff;box-shadow:0 1px 4px rgba(0,0,0,.12);display:flex;align-items:center;justify-content:center;gap:10px}
.badge b{display:block}

/* footer */
.footer{left:0;top:2251px;width:1200px;height:320px;background:var(--foot)}
.sub-title{left:0;top:2300px;width:1200px;text-align:center;color:#fff;font-family:"Montserrat",Arial,sans-serif;font-weight:700;font-size:17px}
.sub-input{left:423px;top:2344px;width:259px;height:35px;background:#3d3d3d;color:#888;font-size:10px;line-height:35px;padding-left:14px}
.sub-btn{left:686px;top:2344px;width:87px;height:35px;border-top:2px solid #fff;border-bottom:2px solid #fff;color:#fff;font-family:"Montserrat",Arial,sans-serif;font-weight:700;font-size:10px;text-align:center;line-height:31px}
.col-head{top:2428px;color:#fff;font-family:"Montserrat",Arial,sans-serif;font-weight:600;font-size:15px;transform:translateX(-50%);white-space:nowrap}
.col-text{color:var(--foot-text);font-size:10px;line-height:19px}
.col-text a{color:#2f8fd6;text-decoration:none}
.bottom{left:0;top:2571px;width:1200px;height:53px;background:var(--foot-deep)}
.copy{left:161px;top:2571px;line-height:53px;color:var(--foot-text);font-size:11px}
.social{top:2585px;width:26px;height:26px;border-radius:50%;background:#fff}
</style>
</head>
<body>

<div class="abs welcome">Welcome To The R.T Harlow Construction LTD</div>
<header class="abs header"></header>
<div class="abs brand">
  <span class="brand-mark"></span>
  <div><div class="brand-name">R.T Harlow</div><div class="brand-sub">CONSTRUCTION LTD</div></div>
</div>
<div class="abs search">SEARCH
  <svg width="12" height="12" viewBox="0 0 12 12"><circle cx="5" cy="5" r="3.6" fill="none" stroke="#555" stroke-width="1.5"/><line x1="7.6" y1="7.6" x2="11" y2="11" stroke="#555" stroke-width="1.6"/></svg>
</div>
<nav class="abs nav">
  <a style="left:374px">CONTACT US</a>
  <a style="left:483px">CASE STUDIES</a>
  <a style="left:593px">TESTIMONIALS</a>
  <a style="left:712px">CERTIFICATIONS</a>
  <a style="left:826px">MEMBERSHIP</a>
</nav>

<div class="abs hero-side hero-left" role="img" aria-label="Modern house at dusk"></div>
<div class="abs hero-side hero-right" role="img" aria-label="Modern house at night"></div>
<div class="abs hero-main" role="img" aria-label="Businessman sketching a city skyline in blue light"></div>
<div class="abs arrow" style="left:139px"><svg width="16" height="14" viewBox="0 0 16 14"><path d="M7 1 1 7l6 6M1 7h14" fill="none" stroke="#333" stroke-width="1.6"/></svg></div>
<div class="abs arrow" style="left:1019px"><svg width="16" height="14" viewBox="0 0 16 14"><path d="M9 1l6 6-6 6M15 7H1" fill="none" stroke="#333" stroke-width="1.6"/></svg></div>

<main>
<div class="abs sheet"></div>

<div class="abs title-row" style="top:646px"><span>R.T Harlow Services</span></div>

<div class="abs service" style="left:268px">
  <svg viewBox="0 0 62 62"><rect x="18" y="4" width="26" height="52" fill="var(--blue)"/><g fill="#fff"><rect x="22" y="10" width="5" height="6"/><rect x="35" y="10" width="5" height="6"/><rect x="22" y="22" width="5" height="6"/><rect x="35" y="22" width="5" height="6"/><rect x="22" y="34" width="5" height="6"/><rect x="35" y="34" width="5" height="6"/><rect x="28" y="46" width="6" height="10"/></g><rect x="6" y="56" width="50" height="3" fill="var(--blue)"/></svg>
  <p>Extensions</p><i></i>
</div>
<div class="abs service" style="left:399px">
  <svg viewBox="0 0 62 62"><path d="M31 6 4 30h8v26h38V30h8z" fill="var(--blue)"/><rect x="26" y="38" width="10" height="18" fill="#fff"/><rect x="16" y="34" width="7" height="7" fill="#fff"/><rect x="40" y="34" width="7" height="7" fill="#fff"/></svg>
  <p>New Build</p><i></i>
</div>
<div class="abs service" style="left:533px">
  <svg viewBox="0 0 62 62"><rect x="4" y="8" width="54" height="48" fill="var(--blue)"/><g stroke="#fff" stroke-width="2"><line x1="4" y1="20" x2="58" y2="20"/><line x1="4" y1="32" x2="58" y2="32"/><line x1="4" y1="44" x2="58" y2="44"/><line x1="22" y1="8" x2="22" y2="20"/><line x1="40" y1="8" x2="40" y2="20"/><line x1="13" y1="20" x2="13" y2="32"/><line x1="31" y1="20" x2="31" y2="32"/><line x1="49" y1="20" x2="49" y2="32"/><line x1="22" y1="32" x2="22" y2="44"/><line x1="40" y1="32" x2="40" y2="44"/><line x1="13" y1="44" x2="13" y2="56"/><line x1="31" y1="44" x2="31" y2="56"/><line x1="49" y1="44" x2="49" y2="56"/></g></svg>
  <p>Garden Wall</p><i></i>
</div>
<div class="abs service" style="left:665px">
  <svg viewBox="0 0 62 62"><path d="M2 48 40 26l14 8-38 22z" fill="var(--blue)"/><path d="M44 28 54 12l4 2-9 17z" fill="var(--blue)"/></svg>
  <p>Plastering</p><i></i>
</div>
<div class="abs service" style="left:798px">
  <svg viewBox="0 0 62 62"><g fill="var(--blue)"><rect x="6" y="30" width="22" height="10"/><rect x="31" y="30" width="22" height="10"/><rect x="6" y="43" width="10" height="10"/><rect x="19" y="43" width="22" height="10"/><rect x="44" y="43" width="9" height="10"/><path d="M34 24 48 6l4 3-12 16z"/></g></svg>
  <p>Brickwork</p><i></i>
</div>
<div class="abs service" style="left:930px">
  <svg viewBox="0 0 62 62"><g fill="var(--blue)"><rect x="10" y="38" width="42" height="18"/><rect x="22" y="8" width="18" height="26"/></g><g stroke="#fff" stroke-width="2"><line x1="10" y1="47" x2="52" y2="47"/><line x1="24" y1="38" x2="24" y2="47"/><line x1="38" y1="38" x2="38" y2="47"/><line x1="31" y1="47" x2="31" y2="56"/></g></svg>
  <p>Groundwork</p><i></i>
</div>

<section>
  <div class="abs case case-one" role="img" aria-label="Timber-framed house with pool at sunset">
    <div class="kicker">Case Studies - 1</div>
    <h3>Lorem Ipsum Dolor Sit Amet</h3>
    <span class="more">READ MORE</span>
  </div>
  <div class="abs case case-two" role="img" aria-label="White modern villa with pool">
    <div class="kicker">Case Studeis - 2</div>
    <h3>Lorem Ipsum Dolor Sit Amet</h3>
    <span class="more">READ MORE</span>
  </div>
</section>

<div class="abs title-row" style="top:1249px"><span>Testimonials</span></div>
<div class="abs card" style="left:219px"><div class="photo" role="img" aria-label="Team of smiling professionals" style="background:linear-gradient(160deg,#5a3a3a,#8d8f98 60%,#c9c9cf)"></div><h4>Lorem Ipsum Dolor Sit Amet</h4><span class="more">Read More</span></div>
<div class="abs card" style="left:477px"><div class="photo" role="img" aria-label="Office worker at a desk" style="background:linear-gradient(160deg,#dfe4ea,#9aa6b4 55%,#3c4350)"></div><h4>Lorem Ipsum Dolor Sit Amet</h4><span class="more">Read More</span></div>
<div class="abs card" style="left:736px"><div class="photo" role="img" aria-label="Colleagues in a bright office" style="background:linear-gradient(160deg,#e5eaf0,#b7c3d1 50%,#6c7f98)"></div><h4>Lorem Ipsum Dolor Sit Amet</h4><span class="more">Read More</span></div>

<div class="abs title-row" style="top:1601px"><span>Contact Us</span></div>
<div class="abs field" style="left:217px;width:189px">Name*</div>
<div class="abs field" style="left:420px;width:182px">Email*</div>
<div class="abs field" style="left:617px;width:167px">Phone Number*</div>
<div class="abs field" style="left:799px;width:182px">Description*</div>
<div class="abs submit">SUBMIT</div>

<section class="abs cert"></section>
<div class="abs title-row" style="top:1866px;left:257px;width:686px"><span style="font-weight:600">Certification &amp; Membership</span></div>
<p class="abs cert-text">R.T Harlow Construction is a registered company with the Quality League of Tradesmen. The QLT has a strict membership criteria &amp; dispute resolution service which gives our clients the confidence to entrust their residential building requirements with R.T Harlow Construction.</p>
<p class="abs cert-sub">QLT Membership means that R.T Harlow Construction Ltd:</p>
<div class="abs tag on" style="left:243px;top:2001px;width:253px">Has a minimum of twelve month trading.</div>
<div class="abs tag" style="left:500px;top:2001px;width:240px">Have provided a professional reference.</div>
<div class="abs tag" style="left:744px;top:2001px;width:211px">Confirmation of business address.</div>
<div class="abs tag" style="left:371px;top:2033px;width:240px">Have provided a professional reference.</div>
<div class="abs tag" style="left:616px;top:2033px;width:211px">Confirmation of business address.</div>
<div class="abs badge" style="left:406px;width:224px" role="img" aria-label="Keystone Pact QLT certification badges">
  <b style="width:42px;height:66px;background:#c8102e"></b>
  <b style="width:140px;height:66px;background:#c8102e"></b>
</div>
<div class="abs badge" style="left:651px;width:141px" role="img" aria-label="QLT membership badge">
  <b style="width:118px;height:66px;background:#b0102a"></b>
</div>
</main>

<footer>
  <div class="abs footer"></div>
  <h2 class="abs sub-title">Subscribe Here</h2>
  <div class="abs sub-input">Email</div>
  <div class="abs sub-btn">SUBSCRIBE</div>

  <div class="abs col-head" style="left:296px">Head Office</div>
  <div class="abs col-text" style="left:161px;top:2457px;width:270px;text-align:center">
    <div>
      <svg width="8" height="10" viewBox="0 0 8 10" style="vertical-align:-1px"><path d="M4 10S0 5.5 0 4a4 4 0 0 1 8 0c0 1.5-4 6-4 6z" fill="#9a9a9a"/></svg>
      Lorem Ipsum Dolor Sit Amet Consectetur Unit</div>
    <div>
      <svg width="9" height="9" viewBox="0 0 9 9" style="vertical-align:-1px"><path d="M2 0 3.5 2.5 2.5 3.5a6 6 0 0 0 3 3l1-1L9 7 8 9C3 8.5.5 6 0 1z" fill="#9a9a9a"/></svg>
      0020 4 555 0182</div>
    <div>
      <svg width="11" height="8" viewBox="0 0 11 8" style="vertical-align:-1px"><rect x=".5" y=".5" width="10" height="7" fill="none" stroke="#2f8fd6"/><path d="M.5.5 5.5 4.5 10.5.5" fill="none" stroke="#2f8fd6"/></svg>
      <a>info@rtharlowbuild.com</a></div>
  </div>

  <div class="abs col-head" style="left:600px">Navigation</div>
  <div class="abs col-text" style="left:555px;top:2457px;text-align:center">Contact Us<br>Case Studies<br>Testimonials</div>
  <div class="abs col-text" style="left:694px;top:2457px;text-align:center">Criffication<br>Membership</div>

  <div class="abs col-head" style="left:929px">About Us</div>
  <div class="abs col-text" style="left:824px;top:2457px;width:210px;text-align:center">Lorem ipsum dolor sit amet, consectetur adipiscing elit, sed do eiusmod tempor incididunt ut labore et dolore magna</div>

  <div class="abs bottom"></div>
  <div class="abs copy">Copyrights ©2018 R.T Harlow Construction. Allrights are Reserved.</div>
  <span class="abs social" style="left:864px"></span>
  <span class="abs social" style="left:893px"></span>
  <span class="abs social" style="left:922px"></span>
  <span class="abs social" style="left:951px"></span>
  <span class="abs social" style="left:980px"></span>
  <span class="abs social" style="left:1009px"></span>
</footer>

</body>
</html>
```